Stationary for a Hand Therapy Clinic
Letterhead/banner, envelopes, business cards
Stationary for a Hand Therapy Clinic - Health
Creative Brief
Professional
Miriam Dorsey, OTD, OTR/L, CHT
Certified Hand Therapist
27548 52nd Ave W Ste 118 Lynnwood, WA 98036
miriam@palmrestcare.example
www.palmrestcare.example
I am open to ideas for placement of: Elbows - Wrists - Fingers (replace dashes with dots) and We guide each step toward fuller days.
We guide each step toward fuller days
miriamdorsey miriamdorsey
Windowed and standard envelopes both are appreciated too! Also, a half sheet sized folder is also great.
One additional item we will need is design for a name tag. Current ones are approximately 1x3" or 1.5x3.5" or so. Likely including the logo, employee's first name and title, such as Certified Hand Therapist, Occupational Therapist, Licensed OT Assistant, Operations Manager, and Patient Care Coordinator.
We definitely prefer orange over green as the primary color for the back side of the business cards and in stationary/other products.
Please use design from entry #439 in our logo contest, replacing dashes with dots. FONT: NEXA BOLD (Or your discretion; others possible) PRIMARY COLORS: ORANGE (#D18122) AND GREEN (#738F52) ACCENT COLORS: BROWN (#544741), LIGHT GREEN (#B9C4AC), RED #993B2C, OR BLUE (#538898) BLACK (#2F3334) WHITE (F0F1E8) PLEASE do not use logos/image from our current website. It will be updated with the new logo.

```html
<!DOCTYPE html>
<html lang="en">
<head>
<meta charset="utf-8">
<title>Palm Rest Care – Name Tag</title>
<link href="https://fonts.googleapis.com/css2?family=Questrial&display=swap" rel="stylesheet">
<style>
  :root {
    --orange: #D18122;
    --green: #738F52;
    --backdrop: #8f8f91;
    --metal-light: #f4f4f4;
    --metal-mid: #dcdcdc;
    --metal-dark: #c4c4c4;
  }
  * { margin: 0; padding: 0; box-sizing: border-box; }
  html, body {
    width: 1200px;
    height: 720px;
    overflow: hidden;
  }
  body {
    background: var(--backdrop);
    font-family: "Questrial", "Helvetica Neue", Arial, sans-serif;
    position: relative;
  }
  .name-tag {
    position: absolute;
    left: 139px;
    top: 156px;
    width: 927px;
    height: 377px;
    border-radius: 34px;
    border: 6px solid var(--orange);
    background:
      linear-gradient(115deg, var(--metal-mid) 0%, var(--metal-light) 30%, var(--metal-mid) 55%, var(--metal-light) 80%, var(--metal-dark) 100%);
  }
  .brand {
    position: absolute;
    left: 400px;
    top: 48px;
    display: flex;
    align-items: center;
    gap: 22px;
  }
  .brand-dot {
    width: 74px;
    height: 74px;
    border-radius: 50%;
    background: var(--green);
    flex: none;
  }
  .brand-text { display: flex; flex-direction: column; }
  .brand-name {
    color: var(--orange);
    font-size: 46px;
    line-height: 1;
    letter-spacing: 1px;
    text-transform: uppercase;
    white-space: nowrap;
  }
  .brand-tagline {
    color: var(--green);
    font-size: 20px;
    letter-spacing: 5px;
    text-transform: uppercase;
    margin-top: 8px;
    white-space: nowrap;
  }
  .wearer {
    position: absolute;
    left: 24px;
    top: 212px;
  }
  .wearer-name {
    color: var(--orange);
    font-size: 44px;
    line-height: 1.1;
  }
  .wearer-title {
    color: var(--green);
    font-size: 26px;
    margin-top: 16px;
  }
</style>
</head>
<body>
  <div class="name-tag">
    <div class="brand">
      <span class="brand-dot"></span>
      <div class="brand-text">
        <span class="brand-name">Palm Rest Care</span>
        <span class="brand-tagline">Elbows • Wrists • Fingers</span>
      </div>
    </div>
    <div class="wearer">
      <p class="wearer-name">Miriam Dorsey</p>
      <p class="wearer-title">Certified Hand Therapist</p>
    </div>
  </div>
</body>
</html>
```